Brightmarket Web Demo Clickthru

Create a realistic web demo to demonstrate our Tradeloop Platform.
There is no back end required.
This Demo will shown to Senior M&A or R&D Executives.
Student entrepreneurs will also see this demo.
There are several attachment to this spec.
Two most important are
Demo User Spec and Demo Flow word documents.
Other attaches are images to give you some idea of the content for specific areas of the site. This will require a walkthrough with selected designer.
Updates

Target Market(s)

See Brief

Industry/Entity Type

Venture Capital

Number of Pages Required

5+ page

Font styles to use
Sans Serif

Colors
32a5d7
33a6d7
0255a3
0692cd
85abd2
f37122
000000
474747
919191

Requirements
Must have
• See Brief
Nice to have
• See Briefs
Should not have
• See Briefs

```html
<!DOCTYPE html>
<html lang="en">
<head>
<meta charset="utf-8">
<title>Brightmarket</title>
<link rel="stylesheet" href="https://fonts.googleapis.com/css2?family=Open+Sans:wght@400;600;700&display=swap">
<style>
:root{
  --blue:#32a5d7;
  --blue-dark:#0255a3;
  --blue-mid:#0692cd;
  --text:#474747;
  --muted:#919191;
  --black:#000000;
  --band:#3a3a3a;
  --footer:#2a2a2a;
  --footer-bar:#1e1e1e;
  --white:#ffffff;
}
*{box-sizing:border-box;margin:0;padding:0}
html,body{width:1200px;height:2280px;overflow:hidden}
body{font-family:"Open Sans",Arial,sans-serif;color:var(--text);background:var(--white);position:relative}
.caps{font-variant:small-caps;letter-spacing:1px}

/* hero */
.hero{position:absolute;left:0;top:0;width:1200px;height:500px;
  background:linear-gradient(100deg,#6a6f73 0%,#b9b4ab 30%,#e4dfd6 55%,#cfc8bd 75%,#8e8a84 100%)}
.search{position:absolute;left:360px;top:190px;width:480px;height:46px;display:flex}
.search-field{flex:1;background:var(--white);border:1px solid #d8d8d8;font-size:15px;color:var(--text);padding:13px 14px}
.search-btn{width:50px;background:var(--blue);display:flex;align-items:center;justify-content:center}
.hero-title{position:absolute;left:0;top:255px;width:1200px;text-align:center;font-size:44px;color:var(--blue);font-weight:400}

/* nav */
.nav{position:absolute;left:0;top:500px;width:1200px;height:60px;background:var(--white);border-bottom:1px solid #e4e4e4;display:flex;align-items:center;padding:0 110px}
.brand{display:flex;align-items:center;gap:10px;font-size:18px;font-weight:700;color:var(--text);width:330px}
.brand-mark{width:24px;height:24px;background:var(--blue)}
.menu{display:flex;list-style:none;font-size:15px;color:var(--text)}
.menu li{padding:8px 12px;border-right:1px solid #ccc;line-height:1}
.menu li:last-child{border-right:0}
.menu .active{background:var(--blue);color:var(--white)}
.login{margin-left:auto;display:flex;align-items:center;gap:10px;font-size:15px}

/* about */
.about{position:absolute;left:0;top:560px;width:1200px;height:400px;text-align:center}
.section-title{font-size:40px;font-weight:400;color:var(--text);margin-top:14px}
.lead{width:960px;margin:8px auto 0;font-size:13px;line-height:20px;color:var(--muted)}
.topics{position:absolute;left:0;top:130px;width:1200px}
.topic{position:absolute;width:240px;height:240px;border-radius:50%;display:flex;flex-direction:column;align-items:center;justify-content:center;color:var(--white)}
.topic h3{font-size:30px;font-weight:400}
.topic p{font-size:13px}
.t1{left:152px;background:radial-gradient(circle,#7fb0c9,#3f6f8a)}
.t2{left:480px;background:radial-gradient(circle,#8fc2d6,#2f7ea0)}
.t3{left:808px;background:radial-gradient(circle,#b89d86,#5c4a3d)}

/* features */
.features{position:absolute;left:0;top:960px;width:1200px;height:380px;background:linear-gradient(90deg,#2f2f2f,#555 50%,#3a3a3a)}
.feature{position:absolute;width:320px;color:var(--white)}
.feature h4{font-size:19px;font-weight:400;display:flex;align-items:center;gap:12px}
.feature p{font-size:13px;line-height:19px;color:#d0d0d0;margin-top:6px;padding-left:40px}
.f1{left:120px;top:60px}.f2{left:480px;top:60px}.f3{left:120px;top:185px}.f4{left:480px;top:185px}
.student-photo{position:absolute;left:880px;top:20px;width:220px;height:360px;background:linear-gradient(180deg,#e8d7c4,#c9a56a 55%,#7a8a9a)}

/* blog */
.blog{position:absolute;left:0;top:1340px;width:1200px;height:300px}
.blog-photo{position:absolute;left:120px;top:30px;width:280px;height:250px;background:linear-gradient(160deg,#d8d2c8,#9aa3a9 60%,#5e6870)}
.blog-body{position:absolute;left:440px;top:28px;width:640px}
.blog-title{font-size:40px;font-weight:400}
.author{font-size:20px;color:var(--text);margin:2px 0 10px}
.blog-body p{font-size:13px;line-height:20px;color:var(--muted)}
.read-more{display:inline-block;margin-top:14px;background:var(--blue);color:var(--white);font-size:12px;padding:7px 14px}

/* partners */
.partners{position:absolute;left:0;top:1640px;width:1200px;height:320px;background:linear-gradient(90deg,#3c3c3c,#5b5b5b 50%,#3c3c3c);text-align:center;color:var(--white)}
.partners .section-title{color:var(--white);margin-top:18px}
.partners .lead{color:#d6d6d6}
.partner-row{position:absolute;left:0;top:190px;width:1200px;display:flex;justify-content:center;gap:90px}
.partner{width:110px;height:80px;display:flex;align-items:center;justify-content:center}
.partner span{display:block;background:#e6e6e6}

/* footer */
.footer{position:absolute;left:0;top:1960px;width:1200px;height:280px;background:var(--footer);color:#bdbdbd;display:flex;padding:30px 110px 0;gap:60px}
.col{width:210px;font-size:12px;line-height:18px}
.col h5{font-size:13px;color:var(--white);font-weight:600;margin-bottom:12px;text-transform:uppercase}
.contact{margin-top:10px;display:flex;align-items:center;gap:8px}
.post{display:flex;gap:10px;margin-bottom:10px}
.thumb{width:44px;height:36px;background:#6b7680;flex:none}
.photos{display:grid;grid-template-columns:repeat(3,56px);gap:8px}
.photos div{height:46px;background:linear-gradient(135deg,#7d8a96,#4d5863)}
.bar{position:absolute;left:0;top:2240px;width:1200px;height:40px;background:var(--footer-bar);color:var(--muted);font-size:11px;display:flex;align-items:center;padding:0 110px}
.top-btn{margin-left:auto;width:28px;height:28px;background:#333;display:flex;align-items:center;justify-content:center}
</style>
</head>
<body>

<header class="hero" role="img" aria-label="Photo of a smiling student in a knit hat working on a laptop in a classroom">
  <div class="search">
    <div class="search-field">Search Course</div>
    <div class="search-btn"><svg width="18" height="18" viewBox="0 0 18 18"><circle cx="7.5" cy="7.5" r="5.5" fill="none" stroke="#fff" stroke-width="2"/><line x1="11.5" y1="11.5" x2="16" y2="16" stroke="#fff" stroke-width="2"/></svg></div>
  </div>
  <h1 class="hero-title caps">We have the largest collection of courses</h1>
</header>

<nav class="nav">
  <div class="brand"><span class="brand-mark"></span>Brightmarket</div>
  <ul class="menu">
    <li>Home</li><li>About</li><li class="active">Student Entrepreneurs</li><li>Blog</li><li>Contact</li>
  </ul>
  <div class="login"><svg width="16" height="16" viewBox="0 0 16 16"><circle cx="8" cy="5" r="3.5" fill="#474747"/><path d="M1 16c0-4 3-6 7-6s7 2 7 6z" fill="#474747"/></svg>Login | Register</div>
</nav>

<section class="about">
  <h2 class="section-title caps">About Brightmarket</h2>
  <p class="lead">Brightmarket connects founders, students and senior executives on one open platform where ideas are shared, tested and funded. Learn from mentors, join live courses and meet partners who can help your venture grow faster.</p>
  <div class="topics">
    <div class="topic t1" role="img" aria-label="Photo of a researcher at work"><h3 class="caps">Research</h3><p>Read More</p></div>
    <div class="topic t2" role="img" aria-label="Photo of an athlete training"><h3 class="caps">Sports</h3><p>Read More</p></div>
    <div class="topic t3" role="img" aria-label="Photo of a student studying"><h3 class="caps">Education</h3><p>Read More</p></div>
  </div>
</section>

<section class="features">
  <div class="feature f1"><h4 class="caps"><svg width="28" height="22" viewBox="0 0 28 22"><rect x="3" y="2" width="22" height="14" fill="#32a5d7"/><rect x="0" y="17" width="28" height="3" fill="#32a5d7"/></svg>Learning Online</h4><p>Study at your own pace with short video lessons, guided tasks and weekly reviews from mentors.</p></div>
  <div class="feature f2"><h4 class="caps"><svg width="28" height="22" viewBox="0 0 28 22"><circle cx="14" cy="6" r="5" fill="#32a5d7"/><path d="M4 22c0-6 4-9 10-9s10 3 10 9z" fill="#32a5d7"/></svg>Pratical Training</h4><p>Work on real business cases and build a pitch that is ready for investors and partners.</p></div>
  <div class="feature f3"><h4 class="caps"><svg width="28" height="22" viewBox="0 0 28 22"><circle cx="8" cy="6" r="4" fill="#32a5d7"/><circle cx="20" cy="6" r="4" fill="#32a5d7"/><path d="M0 22c0-5 3-8 8-8s8 3 8 8zM12 22c0-5 3-8 8-8s8 3 8 8z" fill="#32a5d7"/></svg>Group Seminars</h4><p>Join small groups led by founders and share feedback on ideas in open weekly seminars.</p></div>
  <div class="feature f4"><h4 class="caps"><svg width="28" height="22" viewBox="0 0 28 22"><circle cx="14" cy="5" r="4.5" fill="#32a5d7"/><path d="M6 22l2-12h12l2 12z" fill="#32a5d7"/></svg>Lectures</h4><p>Attend talks from senior executives on funding, research and growing a strong company.</p></div>
  <div class="student-photo" role="img" aria-label="Photo of a student holding yellow folders"></div>
</section>

<section class="blog">
  <div class="blog-photo" role="img" aria-label="Photo of a smiling student with a notebook"></div>
  <div class="blog-body">
    <h2 class="blog-title caps">Blog</h2>
    <div class="author caps">Clara Vance</div>
    <p>Starting a company while still at university taught me more than any class could. In this post I share how our team found its first mentor, tested the idea with real users and prepared a clear pitch. You will also find simple steps to plan your first month, keep the team focused and talk to investors with confidence.</p>
    <span class="read-more">Read More</span>
  </div>
</section>

<section class="partners">
  <h2 class="section-title caps">Our Partners</h2>
  <p class="lead">We work with schools, research labs and investment groups that share our goal of helping new founders succeed. Together we offer courses, events and funding paths for every stage of a young venture, from first idea to growth.</p>
  <div class="partner-row">
    <div class="partner"><span style="width:70px;height:60px"></span></div>
    <div class="partner"><span style="width:110px;height:34px"></span></div>
    <div class="partner"><span style="width:60px;height:70px"></span></div>
    <div class="partner"><span style="width:80px;height:70px;border-radius:50%"></span></div>
    <div class="partner"><span style="width:110px;height:34px"></span></div>
  </div>
</section>

<footer class="footer">
  <div class="col"><h5>About us</h5><p>Brightmarket is an open space where students and leaders meet to learn, build and fund new ideas together.</p>
    <div class="contact"><svg width="10" height="14" viewBox="0 0 10 14"><path d="M5 0a5 5 0 0 1 5 5c0 4-5 9-5 9S0 9 0 5a5 5 0 0 1 5-5z" fill="#32a5d7"/></svg>Harbor Street, Easton</div>
    <div class="contact"><svg width="12" height="10" viewBox="0 0 12 10"><rect width="12" height="10" fill="#32a5d7"/><path d="M0 0l6 5 6-5" fill="none" stroke="#2a2a2a"/></svg>hello@brightmarket.example</div></div>
  <div class="col"><h5>Testimonials</h5><p>"A great place to find mentors and test ideas with real people."</p><p style="margin-top:8px;color:var(--blue)">— Member, Class of 2024</p></div>
  <div class="col"><h5>Recent posts</h5>
    <div class="post"><div class="thumb"></div><p>First steps for new founders<br>May 12</p></div>
    <div class="post"><div class="thumb"></div><p>How to plan a short pitch<br>May 08</p></div>
    <div class="post"><div class="thumb"></div><p>Meet our spring mentors<br>May 02</p></div></div>
  <div class="col"><h5>Photos</h5><div class="photos" role="img" aria-label="Gallery of event photos"><div></div><div></div><div></div><div></div><div></div><div></div></div></div>
</footer>
<div class="bar">© 2025 Brightmarket. All rights reserved.
  <div class="top-btn"><svg width="12" height="8" viewBox="0 0 12 8"><path d="M1 7l5-5 5 5" fill="none" stroke="#fff" stroke-width="2"/></svg></div>
</div>

</body>
</html>
```